Auto glass company

THRIFTWAY
Roving Auto Glass, LLC
555-604-1973

* Windshield Replacement
* Rock Chip Repair
Danny "K"
Thriftwayrovingautoglass@mailbox-demo.net
* Fully Insured

This is what I would like on the card. The image is what I had before. Looking for a logo possible too, couldn’t find a place to add that on. It’s a auto glass company.

Target Market(s)

Auto glass

Industry/Entity Type

Auto glass

Contact Information for Business Card

Logo, business name, phone number, windshield replacement, rock chip repair, insured, owner name Danny K, email address thriftwayrovingautoglass@mailbox-demo.net

Colors

Designer to choose colors to be used in the design.

Requirements
Must have
• Logo, business name, phone number, windshield replacement, rock chip repair, insured, owner name Danny K, email address thriftwayrovingautoglass@mailbox-demo.net

```html
<!DOCTYPE html>
<html lang="en">
<head>
<meta charset="utf-8">
<title>Thriftway Roving Auto Glass – Business Card</title>
<link rel="stylesheet" href="https://fonts.googleapis.com/css2?family=Jost:wght@400;500;700;800&display=swap">
<style>
  :root {
    --navy: #0b2f6b;
    --orange: #f5a300;
    --card-light: #f4f5fa;
    --card-shade: #d9dcec;
    --page: #e9e7e2;
    --white: #ffffff;
  }
  * { box-sizing: border-box; margin: 0; padding: 0; }
  html, body { width: 1200px; height: 1040px; overflow: hidden; }
  body {
    background: var(--page);
    font-family: "Jost", "Helvetica Neue", Arial, sans-serif;
    position: relative;
  }
  .card {
    position: absolute;
    left: 200px;
    width: 800px;
    height: 457px;
    border-radius: 26px;
    overflow: hidden;
    background: linear-gradient(160deg, var(--white) 0%, var(--card-light) 40%, var(--card-shade) 65%, var(--card-light) 85%, var(--white) 100%);
    box-shadow: 0 14px 30px rgba(0,0,0,0.18);
  }
  .card-front { top: 40px; }
  .card-back { top: 543px; }

  .wave { position: absolute; inset: 0; width: 100%; height: 100%; }

  .brand {
    position: absolute;
    color: var(--navy);
    font-weight: 800;
    line-height: 1;
    display: flex;
    align-items: center;
    gap: 12px;
  }
  .brand-square {
    width: 18px; height: 18px;
    background: var(--orange);
    flex: none;
  }
  .brand-name { display: flex; flex-direction: column; }
  .brand-word { letter-spacing: -0.01em; }
  .brand-sub { letter-spacing: 0.14em; text-transform: uppercase; margin-top: 8px; }

  .card-front .brand { left: 40px; top: 185px; gap: 10px; }
  .card-front .brand-square { width: 14px; height: 14px; }
  .card-front .brand-word { font-size: 48px; }
  .card-front .brand-sub { font-size: 15px; margin-top: 7px; }

  .contact {
    position: absolute;
    right: 44px;
    top: 70px;
    text-align: right;
    color: var(--white);
  }
  .owner-name { font-size: 36px; font-weight: 700; letter-spacing: 0.01em; }
  .owner-title { font-size: 17px; font-weight: 400; color: var(--orange); letter-spacing: 0.06em; margin-top: 2px; }
  .contact-line {
    display: flex; align-items: center; justify-content: flex-end; gap: 10px;
    margin-top: 26px;
  }
  .phone { font-size: 32px; font-weight: 400; }
  .email { font-size: 16px; font-weight: 400; margin-top: 14px; }
  .icon { width: 20px; height: 20px; flex: none; }

  .card-back .brand { left: 50%; top: 120px; transform: translateX(-50%); }
  .card-back .brand-word { font-size: 104px; }
  .card-back .brand-sub { font-size: 31px; margin-top: 12px; }

  .services {
    position: absolute;
    left: 0; right: 0; bottom: 70px;
    display: flex; justify-content: center; align-items: center; gap: 12px;
    color: var(--navy);
    font-size: 19px;
    letter-spacing: 0.04em;
    text-transform: uppercase;
    list-style: none;
  }
  .services li { display: flex; align-items: center; gap: 12px; }
  .tick { width: 16px; height: 16px; flex: none; }
</style>
</head>
<body>

<section class="card card-front" aria-label="Business card front">
  <svg class="wave" viewBox="0 0 800 457" preserveAspectRatio="none" aria-hidden="true">
    <path transform="translate(-24 0)" fill="#f5a300" d="M540 0 C440 10 440 200 370 310 C320 390 250 440 190 457 L800 457 L800 0 Z"/>
    <path transform="translate(-12 0)" fill="#ffffff" d="M540 0 C440 10 440 200 370 310 C320 390 250 440 190 457 L800 457 L800 0 Z"/>
    <path fill="#0b2f6b" d="M540 0 C440 10 440 200 370 310 C320 390 250 440 190 457 L800 457 L800 0 Z"/>
  </svg>

  <div class="brand">
    <span class="brand-square"></span>
    <span class="brand-name">
      <span class="brand-word">THRIFTWAY</span>
      <span class="brand-sub">Roving Auto Glass, LLC</span>
    </span>
  </div>

  <div class="contact">
    <p class="owner-name">DANNY K</p>
    <p class="owner-title">OWNER</p>
    <p class="contact-line phone">
      <span>555-604-1973</span>
      <svg class="icon" viewBox="0 0 24 24" aria-label="Phone"><path fill="#f5a300" d="M6.6 10.8a15.1 15.1 0 0 0 6.6 6.6l2.2-2.2a1 1 0 0 1 1-.25 11.4 11.4 0 0 0 3.6.57 1 1 0 0 1 1 1V20a1 1 0 0 1-1 1A17 17 0 0 1 3 4a1 1 0 0 1 1-1h3.5a1 1 0 0 1 1 1c0 1.25.2 2.45.57 3.57a1 1 0 0 1-.25 1z"/></svg>
    </p>
    <p class="contact-line email">
      <span>thriftwayrovingautoglass@mailbox-demo.net</span>
      <svg class="icon" viewBox="0 0 24 24" aria-label="Email"><rect x="2" y="5" width="20" height="14" rx="1.5" fill="#f5a300"/><path d="M3 6.5l9 6.5 9-6.5" fill="none" stroke="#0b2f6b" stroke-width="1.8"/></svg>
    </p>
  </div>
</section>

<section class="card card-back" aria-label="Business card back">
  <div class="brand">
    <span class="brand-square"></span>
    <span class="brand-name">
      <span class="brand-word">THRIFTWAY</span>
      <span class="brand-sub">Roving Auto Glass, LLC</span>
    </span>
  </div>

  <ul class="services">
    <li>Windshield Replacement</li>
    <li>
      <svg class="tick" viewBox="0 0 16 16" aria-hidden="true"><rect x="1" y="1" width="14" height="14" fill="none" stroke="#f5a300" stroke-width="2"/><path d="M4 8l3 3 5-6" fill="none" stroke="#f5a300" stroke-width="2"/></svg>
      Rock Chip Repair
    </li>
    <li>
      <svg class="tick" viewBox="0 0 16 16" aria-hidden="true"><rect x="1" y="1" width="14" height="14" fill="none" stroke="#f5a300" stroke-width="2"/><path d="M4 8l3 3 5-6" fill="none" stroke="#f5a300" stroke-width="2"/></svg>
      Fully Insured
    </li>
  </ul>
</section>

</body>
</html>
```